Bref créative
BrightHollow Capital Partners
......putting entrepreneurs and investors together
Professional
Marcus Pellow
418 Weldon Avenue
Suite 340
Media, PA 19087
brighthollowcap@mailvista.net
I have selected the black & red color scheme on the logo.
Angel Investors/Angel Funds
Seed/Start-up Investment
Private Equity Funds
Venture Capital Funding
Merchant Funding
Receivable/Purchase Order Funding

```html
<!DOCTYPE html>
<html lang="en">
<head>
<meta charset="utf-8">
<title>BrightHollow Capital Partners – Stationery Set</title>
<link href="https://fonts.googleapis.com/css2?family=Lato:wght@400;700&display=swap" rel="stylesheet">
<style>
:root{
  --backdrop:#2e2e2f;
  --paper:#ffffff;
  --red:#e0262b;
  --ink:#222222;
  --grey:#8a8a8a;
  --caption:#b9b9b9;
  --black:#161616;
}
*{margin:0;padding:0;box-sizing:border-box}
html,body{width:1200px;height:338px;overflow:hidden;background:var(--backdrop)}
body{position:relative;font-family:'Lato',sans-serif;color:var(--ink)}
.item{position:absolute;background:var(--paper);overflow:hidden;box-shadow:0 1px 3px rgba(0,0,0,.5)}
.caption{position:absolute;font-size:5px;color:var(--caption);letter-spacing:.3px;white-space:nowrap}
.brand{font-family:'Lato',sans-serif;font-weight:700;color:var(--red);letter-spacing:.6px;white-space:nowrap}
.brand-mark{display:inline-block;width:5px;height:5px;border-radius:50%;background:var(--red);margin-right:3px;vertical-align:middle}
.tagline{font-size:3.6px;color:var(--grey);white-space:nowrap}
.fine{font-size:3.6px;color:var(--grey);line-height:1.5;white-space:nowrap}
.item svg.shape{position:absolute;inset:0;width:100%;height:100%}

/* business cards */
.card-front{left:7px;top:168px;width:58px;height:79px}
.card-front .brand{position:absolute;left:6px;top:12px;font-size:5px}
.card-front .name{position:absolute;left:6px;top:34px;font-size:4.4px;font-weight:700}
.card-front .fine{position:absolute;left:6px;top:42px}
.card-back{left:7px;top:259px;width:58px;height:39px}
.card-back .brand{position:absolute;left:14px;top:9px;font-size:4.4px}
.card-back .fine{position:absolute;left:14px;top:18px;font-size:3px}

/* letterheads */
.letterhead{top:12px;width:221px;height:300px}
.letterhead-one{left:151px}
.letterhead-two{left:391px}
.letterhead .brand{position:absolute;top:18px;font-size:8px}
.letterhead-one .brand{left:32px}
.letterhead-two .brand{left:30px}
.letterhead .contact{position:absolute;right:18px;top:16px;text-align:right}
.letterhead .footer{position:absolute;bottom:10px;left:0;right:0;text-align:center}

/* envelopes front */
.envelope{left:631px;width:228px}
.envelope-one{top:108px;height:91px}
.envelope-two{top:228px;height:86px}
.envelope .brand{position:absolute;left:12px;top:12px;font-size:7px}
.envelope .tagline{position:absolute;left:12px;top:22px}
.envelope .footer{position:absolute;left:0;right:0;bottom:6px;text-align:center}

/* envelope backs */
.env-back-red{left:883px;top:101px;width:310px;height:91px;background:var(--paper)}
.env-back-red .brand{position:absolute;left:50%;top:20px;transform:translateX(-50%);color:var(--paper);font-size:8px}
.env-back-black{left:883px;top:194px;width:310px;height:53px}
.env-back-white{left:883px;top:250px;width:310px;height:64px}
.env-back-white .brand{position:absolute;left:50%;top:12px;transform:translateX(-50%);font-size:7px}
</style>
</head>
<body>

<!-- Business cards -->
<p class="caption" style="left:7px;top:158px">Business Card Front</p>
<div class="item card-front">
  <svg class="shape" viewBox="0 0 58 79" preserveAspectRatio="none"><path d="M0 0h3q3 40 0 79H0z" fill="var(--red)"/></svg>
  <div class="brand">BRIGHTHOLLOW</div>
  <div class="name">Marcus Pellow</div>
  <div class="fine">418 Weldon Avenue<br>Suite 340<br>Media, PA 19087<br>brighthollowcap@mailvista.net</div>
</div>
<p class="caption" style="left:7px;top:250px">Business Card Back</p>
<div class="item card-back">
  <svg class="shape" viewBox="0 0 58 39" preserveAspectRatio="none"><rect x="4" y="8" width="7" height="7" fill="var(--red)"/></svg>
  <div class="brand">BRIGHTHOLLOW</div>
  <div class="fine">Capital Partners</div>
</div>

<!-- Letterhead 1 -->
<div class="item letterhead letterhead-one">
  <svg class="shape" viewBox="0 0 221 300" preserveAspectRatio="none">
    <path d="M0 0h22q-14 80 -4 170Q6 110 0 150z" fill="var(--red)"/>
    <path d="M221 0v40q-6-20-3-40z" fill="var(--red)"/>
  </svg>
  <div class="brand">BRIGHTHOLLOW</div>
  <div class="contact fine">418 Weldon Avenue<br>Suite 340<br>Media, PA 19087</div>
  <div class="footer fine">418 Weldon Avenue, Suite 340, Media, PA 19087 · brighthollowcap@mailvista.net</div>
</div>
<p class="caption" style="left:151px;top:315px">Letterhead Version 1</p>

<!-- Letterhead 2 -->
<div class="item letterhead letterhead-two">
  <svg class="shape" viewBox="0 0 221 300" preserveAspectRatio="none">
    <path d="M0 0h14q-10 20 -14 40z" fill="var(--red)"/>
    <path d="M221 0h-22q14 80 4 170Q215 110 221 150z" fill="var(--red)"/>
  </svg>
  <div class="brand">BRIGHTHOLLOW</div>
  <div class="footer fine">418 Weldon Avenue, Suite 340, Media, PA 19087 · brighthollowcap@mailvista.net</div>
</div>
<p class="caption" style="left:391px;top:315px">Letterhead Version 2</p>

<!-- Envelopes front -->
<div class="item envelope envelope-one">
  <div class="brand">BRIGHTHOLLOW</div>
  <div class="tagline">putting entrepreneurs and investors together</div>
  <div class="footer fine">418 Weldon Avenue, Suite 340, Media, PA 19087</div>
</div>
<p class="caption" style="left:631px;top:202px">Envelope Version 1</p>
<div class="item envelope envelope-two">
  <svg class="shape" viewBox="0 0 228 86" preserveAspectRatio="none"><path d="M0 0h4v86H0z" fill="var(--red)"/></svg>
  <div class="brand">BRIGHTHOLLOW</div>
  <div class="tagline">putting entrepreneurs and investors together</div>
  <div class="footer fine">418 Weldon Avenue, Suite 340, Media, PA 19087</div>
</div>
<p class="caption" style="left:631px;top:317px">Envelope Version 2</p>

<!-- Envelope backs -->
<div class="item env-back-red">
  <svg class="shape" viewBox="0 0 310 91" preserveAspectRatio="none">
    <path d="M0 0h310v50L175 88q-20 5-40 0L0 50z" fill="var(--red)"/>
  </svg>
  <div class="brand">BRIGHTHOLLOW</div>
</div>
<div class="item env-back-black">
  <svg class="shape" viewBox="0 0 310 53" preserveAspectRatio="none">
    <rect width="310" height="53" fill="var(--paper)"/>
    <path d="M0 0h310v28L175 50q-20 4-40 0L0 28z" fill="var(--black)"/>
  </svg>
</div>
<div class="item env-back-white">
  <svg class="shape" viewBox="0 0 310 64" preserveAspectRatio="none">
    <path d="M0 0L150 40q5 2 10 0L310 0M0 64L130 34M310 64L180 34" fill="none" stroke="#d6d6d6" stroke-width="0.8"/>
  </svg>
  <div class="brand">BRIGHTHOLLOW</div>
</div>
<p class="caption" style="left:1000px;top:317px">Envelope Back View</p>

</body>
</html>
```